Cleaning Company needs a new business card design

Hi, We are looking for new business card designs to update with our latest logo and company information.
We would like to see designs using the colours:
Royal Blue #4169E1 - this is our company colour so this has to be in there. Please feel free to experiment with other colours.
Must include:
Front of business card:
Logo
Back of the business card:
0800 529 6081
07438 915 702
Email: info@pkrtidyhomes.co.uk
Web: www.pkrtidyhomes.co.uk
Services:
End of Tenancy
Carpet & Upholstery
Regular & One Off
all work fully insured.
The front of the business card with the logo can be made to look raised print. The blue man to be a shiny finish.
The business card needs to be presented in a matt finish
The business must be in the following styles:
Standard Square with rounded corners.
Thank you to all that take part in this.
Target Market(s)
Men and Women of different ages in the UK.
Industry/Entity Type
House Cleaning
Contact Information for Business Card
Front of business card:
Logo
0800 529 6081
07438 915 702
Email: pkrtidy@mailbox-demo.co.uk
Services:
End of Tenancy
Carpet & Upholstery
Regular & One Off
all work fully insured.

```html
<!DOCTYPE html>
<html lang="en">
<head>
<meta charset="utf-8">
<title>PKR Tidy Homes – Business Cards</title>
<link href="https://fonts.googleapis.com/css2?family=Open+Sans:wght@400;600;700&display=swap" rel="stylesheet">
<style>
  :root {
    --backdrop: #8e8e8e;
    --card-black: #111111;
    --card-black-light: #1e1e1e;
    --royal-blue: #3b4fb8;
    --sky-blue: #1ea6df;
    --text-white: #f2f2f2;
    --divider: #2c2c2c;
  }
  * { box-sizing: border-box; margin: 0; padding: 0; }
  html, body { width: 1200px; height: 900px; overflow: hidden; }
  body {
    position: relative;
    background: var(--backdrop);
    font-family: "Open Sans", Arial, sans-serif;
  }
  .card {
    position: absolute;
    border-radius: 14px;
    background: radial-gradient(circle at 65% 35%, var(--card-black-light), var(--card-black) 70%);
    box-shadow: 0 10px 24px rgba(0,0,0,0.35);
    overflow: hidden;
  }
  /* Front: logo side */
  .card-front {
    left: 500px; top: 90px;
    width: 560px; height: 360px;
    display: flex; align-items: center; justify-content: center; gap: 14px;
  }
  .brand-dot {
    width: 22px; height: 22px; border-radius: 50%;
    background: var(--royal-blue);
  }
  .brand-name {
    color: var(--royal-blue);
    font-weight: 700;
    font-size: 34px;
    letter-spacing: 0.5px;
  }
  /* Back: contact side */
  .card-back {
    left: 150px; top: 400px;
    width: 620px; height: 400px;
  }
  .figure-area {
    position: absolute;
    left: 0; top: 30px;
    width: 270px; height: 370px;
    background: var(--sky-blue);
    border-radius: 0 120px 0 14px;
  }
  .contact-list {
    position: absolute;
    right: 28px; top: 108px;
    list-style: none;
    text-align: right;
    color: var(--text-white);
    font-size: 17px;
    line-height: 25px;
  }
  .contact-list li { display: flex; justify-content: flex-end; align-items: center; gap: 10px; }
  .contact-icon { width: 14px; height: 14px; fill: var(--sky-blue); flex: none; }
  .divider {
    position: absolute;
    left: 350px; right: 40px; top: 218px;
    height: 1px; background: var(--divider);
  }
  .services {
    position: absolute;
    right: 52px; top: 232px;
    text-align: right;
    color: var(--text-white);
    font-size: 19px;
    line-height: 24px;
  }
  .services-title { color: var(--sky-blue); font-weight: 700; font-size: 20px; margin-bottom: 2px; }
  .services-list { list-style: none; }
  .insured { font-size: 20px; margin-top: 10px; margin-right: -22px; }
</style>
</head>
<body>

  <section class="card card-back" aria-label="Business card back">
    <div class="figure-area" role="img" aria-label="Large cleaner figure pushing a vacuum"></div>

    <ul class="contact-list">
      <li>0800 529 6081
        <svg class="contact-icon" viewBox="0 0 16 16"><path d="M3 1l3 3-2 2c1 2 3 4 5 5l2-2 3 3-2 3C6 15 1 10 1 3z"/></svg>
      </li>
      <li>07438 915 702
        <svg class="contact-icon" viewBox="0 0 16 16"><rect x="4" y="1" width="8" height="14" rx="1.5"/><rect x="5.5" y="3" width="5" height="8" fill="#111"/></svg>
      </li>
      <li>pkrtidy@mailbox-demo.co.uk
        <svg class="contact-icon" viewBox="0 0 16 16"><rect x="1" y="3" width="14" height="10" rx="1"/><path d="M1 4l7 5 7-5" stroke="#111" stroke-width="1.4" fill="none"/></svg>
      </li>
      <li>www.pkrtidyhomes.co.uk
        <svg class="contact-icon" viewBox="0 0 16 16"><circle cx="8" cy="8" r="7"/><path d="M1 8h14M8 1c3 3 3 11 0 14M8 1c-3 3-3 11 0 14" stroke="#111" stroke-width="1.2" fill="none"/></svg>
      </li>
    </ul>

    <div class="divider"></div>

    <div class="services">
      <h2 class="services-title">Services</h2>
      <ul class="services-list">
        <li>End of Tenancy</li>
        <li>Carpet &amp; Upholstery</li>
        <li>Regular &amp; One Off</li>
      </ul>
      <p class="insured">All work fully insured.</p>
    </div>
  </section>

  <section class="card card-front" aria-label="Business card front">
    <span class="brand-dot"></span>
    <h1 class="brand-name">PKR Tidy Homes Limited</h1>
  </section>

</body>
</html>
```